Design website for new email startup

We are starting a company called Posta.QZ (it will live at http://posta.qz.example).

We would like the main landing page for our site designed. We have provided a very simple wireframe to help provide direction for the content it should include, but we do not expect the designers to adhere to it at all - we encourage unique ideas. There is some sample text in the wireframe - this does not have to be used, but may provide ideas.

We provide an easy way for people to manage email for a custom domain name. For example if you own "myfamilyword.example" you can point your DNS records to us and we'll make it easy to have emails addressed to your domain get forwarded to your existing email (vexmail, etc). Folks running blogs, and other small sites can quickly setup email addresses for their domains and manage them in one place.

(For technical folks, we have you point your dns mx records to us, hence the name. That way all your email hits us and we can redirect it wherever you want. We make it easy to manage a single domain or a bunch of domains. Many domain registrars offer this service for a fee, and have clumsy management tools. We provide a robust simple toolset for free, as well as premium options).

The goal of the landing page is to get folks into the signup flow. The second priority flow is to have them take a look at the premium plan offerings.

We may offer the winning designer additional work for the remainder of the site design.
Updates

I've changed this project to a committed payment.  It is no longer refundable.  Thank you.

Target Market(s)

Bloggers, podcasters, designers, app developers - people who are a little tech savvy.

Industry/Entity Type

It Company

Font styles to use
Sans Serif

Colors

Designer to choose colors to be used in the design.

Requirements
Must have
• A full fidelity mockup (comp) of the landing page including the source file (psd, ai, etc).

Some sort of logo treatment for the posta.qz brand

A call to action for signup, such as the suggested 'Get Started Here'
Nice to have
• A hip startup feel

Incorporation of the email theme

Give the impression it is simple, easy and fast

```html
<!DOCTYPE html>
<html lang="en">
<head>
<meta charset="utf-8">
<title>Posta.QZ — We Make Email Easy</title>
<link rel="stylesheet" href="https://fonts.googleapis.com/css2?family=Open+Sans:wght@400;600;700;800&family=Open+Sans+Condensed:wght@300&display=swap">
<style>
  :root {
    --header-bg: #474747;
    --nav-text: #e4e4e4;
    --nav-blue: #3f9bd6;
    --nav-orange: #f1a13f;
    --nav-coral: #f08a6d;
    --sky-deep: #0d5aa5;
    --sky-mid: #2a7dcc;
    --sky-light: #64aee9;
    --white: #ffffff;
    --button-light: #f4f4f2;
    --button-light-text: #0f5191;
    --button-dark: #3c3c3c;
    --or-text: #1e2a33;
    --body-text: #4a4a4a;
    --muted-text: #7a7a7a;
    --divider: #3f86b8;
    --partner-one: #f08a23;
    --partner-two: #1a1a1a;
    --footer-bg: #1c1c1c;
    --footer-text: #f0f0f0;
  }
  * { box-sizing: border-box; margin: 0; padding: 0; }
  html, body { width: 1200px; height: 850px; overflow: hidden; }
  body { font-family: "Open Sans", Arial, sans-serif; background: var(--white); position: relative; }

  .site-header { position: absolute; left: 0; top: 0; width: 1200px; height: 75px; background: var(--header-bg); }
  .brand { position: absolute; left: 203px; top: 13px; font-size: 37px; font-weight: 700; color: var(--white); letter-spacing: -1px; }
  .main-nav { position: absolute; left: 804px; top: 0; display: flex; gap: 3px; }
  .main-nav a { display: block; width: 64px; height: 75px; padding-top: 48px; text-align: center; font-family: "Open Sans Condensed", "Open Sans", sans-serif; font-size: 12.5px; color: var(--nav-text); text-decoration: none; border-bottom: 4px solid; }
  .main-nav .nav-how { border-color: var(--nav-blue); font-size: 11.5px; letter-spacing: -0.3px; }
  .main-nav .nav-support { border-color: var(--nav-orange); }
  .main-nav .nav-login { border-color: var(--nav-coral); }

  .hero { position: absolute; left: 0; top: 75px; width: 1200px; height: 487px; text-align: center; color: var(--white); }
  .hero-backdrop { position: absolute; inset: 0; background:
      radial-gradient(ellipse 500px 120px at 700px 260px, rgba(150,200,245,0.35), transparent),
      radial-gradient(ellipse 400px 90px at 1050px 120px, rgba(160,210,250,0.45), transparent),
      linear-gradient(100deg, var(--sky-deep) 0%, var(--sky-mid) 55%, var(--sky-light) 100%); }
  .hero-content { position: relative; }
  .hero-title { padding-top: 83px; font-size: 46px; font-weight: 800; letter-spacing: -1.8px; line-height: 1; }
  .hero-lines { margin-top: 9px; font-family: "Open Sans Condensed", "Open Sans", sans-serif; font-size: 15.5px; line-height: 25.5px; letter-spacing: -0.2px; }
  .cta { display: block; width: 235px; height: 40px; margin: 0 auto; border-radius: 4px; font-size: 20px; font-weight: 700; line-height: 40px; text-decoration: none; box-shadow: 0 2px 3px rgba(0,0,0,0.3); }
  .cta-signup { margin-top: 69px; background: var(--button-light); color: var(--button-light-text); letter-spacing: -0.3px; }
  .cta-or { margin: 9px 0 8px; font-size: 20px; font-weight: 700; color: var(--or-text); line-height: 21px; }
  .cta-plans { background: var(--button-dark); color: var(--white); letter-spacing: 0.6px; border: 1px solid #2a2a2a; }

  .partners { position: absolute; left: 0; top: 562px; width: 1200px; height: 228px; }
  .partner { position: absolute; top: 16px; width: 300px; text-align: center; }
  .partner-left { left: 249px; }
  .partner-right { left: 649px; }
  .partner-title { font-size: 14px; line-height: 17px; color: var(--body-text); letter-spacing: 0.1px; }
  .partner-mark { height: 128px; display: flex; align-items: center; justify-content: center; gap: 10px; font-size: 30px; font-weight: 800; letter-spacing: -0.5px; }
  .partner-left .partner-mark { color: var(--partner-one); }
  .partner-right .partner-mark { color: var(--partner-two); }
  .mark-dot { width: 26px; height: 26px; border-radius: 50%; background: currentColor; }
  .readmore { display: block; margin-top: 7px; font-size: 11.5px; color: var(--muted-text); text-decoration: none; letter-spacing: 0.2px; }
  .partners-divider { position: absolute; left: 599px; top: 30px; width: 2px; height: 155px; background: var(--divider); }

  .site-footer { position: absolute; left: 0; top: 790px; width: 1200px; height: 60px; background: var(--footer-bg); color: var(--footer-text); text-align: center; font-size: 12px; line-height: 60px; }
</style>
</head>
<body>
  <header class="site-header">
    <div class="brand">Posta.QZ</div>
    <nav class="main-nav">
      <a class="nav-how" href="#">How It Works</a>
      <a class="nav-support" href="#">Support</a>
      <a class="nav-login" href="#">Login</a>
    </nav>
  </header>

  <section class="hero">
    <div class="hero-backdrop" role="img" aria-label="Photograph of a deep blue sky with soft streaks of white cloud"></div>
    <div class="hero-content">
      <h1 class="hero-title">WE MAKE EMAIL EASY</h1>
      <p class="hero-lines">
        Give Us Five Minutes And We’ll Get You Email Form Your Domain<br>
        Easily Forward Mail Form Your Custom Domain Name Whererver&nbsp; You Want It<br>
        You Take The Mail, We’ll Keep The Spam
      </p>
      <a class="cta cta-signup" href="#">GET STARTED FREE</a>
      <div class="cta-or">OR</div>
      <a class="cta cta-plans" href="#">COMPARE PLANS</a>
    </div>
  </section>

  <section class="partners">
    <div class="partner partner-left">
      <p class="partner-title">How to configure your SkyShield DNS to use<br>POSTA.QZ</p>
      <div class="partner-mark"><span class="mark-dot"></span>SkyShield</div>
      <a class="readmore" href="#">READMORE</a>
    </div>
    <div class="partners-divider"></div>
    <div class="partner partner-right">
      <p class="partner-title">Use posta with your DomainPapa domain<br>registration for reliable email forwarding</p>
      <div class="partner-mark">DomainPapa</div>
      <a class="readmore" href="#">READMORE</a>
    </div>
  </section>

  <footer class="site-footer">Copyright 2014&nbsp; Posta.QZ | All Rights Reserved | Powered by Posta.QZ</footer>
</body>
</html>
```